Lorvika.no is a new website about pedagogical entrepreneurship. It's main target group is teachers. The Fjellmark Institute for Classroom Media and the Nordvik Agency for Schools and Study are leading the project.

The web page is meant to show examples of how different methods of entrepreneurship can be used pedagogical in a learning environment. The page will also support the user with examples of different teaching programs and other examples of best practice.

Pedagogical entrepreneurship is not about business and men in suits. It's a method for learning. The focus in the design should be on school, education and new ways of learning.

The final product should be motivating and engaging, but at the same time governmental and serious. We are not looking for something "flashy" and corporate-looking, but a moderate, task-focused and clean design that state quality.

We need designs for three pages:
1 - frontpage
2 - subpage ("Metoder og undervisningsopplegg")
3 - subpage ("Smått-VERK i Brekkelia")

The interaction design for these three pages will be uploaded as an attachment.

We would like you to find inspiration in the following websites:
- www.gryvekst.no
- www.lavrek.no
- www.tovandstudio.com
- www.kvp.no
(more will be added)

Please use the attached logo, and feel free to use this as an inspiration for the rest of the design.

Target Market(s)

Teachers

Industry/Entity Type

Education

Requirements
Must have
• * Header with: Logo. Main navigation. Utility navigation. Search box.
* Footer
Should not have
• Images of men in suits.
Very strong graphical elements that stands out too much (we want it clean).

```html
<!DOCTYPE html>
<html lang="en">
<head>
<meta charset="utf-8">
<title>Lorvika.no – Pedagogical entrepreneurship</title>
<link rel="stylesheet" href="https://fonts.googleapis.com/css2?family=PT+Sans:ital,wght@0,400;0,700;1,400&family=Noto+Serif:ital,wght@1,400;1,700&display=swap">
<style>
:root{
  --page-grey:#e6e6e6;
  --header-top:#1f5f99;
  --header-bottom:#0b2f58;
  --nav-blue:#7fd2f7;
  --panel-blue:#1e80c9;
  --panel-blue-dark:#12609f;
  --orange:#f7901e;
  --orange-dark:#e8741a;
  --green:#6f9e20;
  --green-dark:#527d16;
  --rust:#c9521f;
  --rust-dark:#a93e16;
  --link-blue:#1a72bd;
  --text-dark:#1b1b1b;
  --text-mid:#333;
  --box-grey:#efefef;
  --line-grey:#dcdcdc;
  --carousel:#3b94e2;
  --carousel-edge:#1d5e9e;
  --footer-top:#1d62a6;
  --footer-bottom:#0b3c7c;
  --footer-link:#cfe0f2;
  --accent-yellow:#f4d22c;
  --search-green:#6bb52a;
}
*{box-sizing:border-box;margin:0;padding:0}
html,body{width:868px;height:1200px;overflow:hidden}
body{position:relative;background:#fff;font-family:"PT Sans",Arial,sans-serif;color:var(--text-dark)}
.abs{position:absolute}
.top-band{left:0;top:0;width:868px;height:456px;background:var(--page-grey)}

/* header */
.site-header{left:20px;top:18px;width:828px;height:382px;border-radius:6px;
  background:linear-gradient(180deg,var(--header-top) 0%,#164b80 55%,var(--header-bottom) 100%)}
.brand{left:112px;top:30px;display:flex;align-items:center;gap:10px}
.brand-mark{width:46px;height:46px;border-radius:50%;background:#5bb8ee}
.brand-name{font-size:38px;font-weight:700;color:#5bb8ee;line-height:1}
.brand-tagline{left:181px;top:70px;font-size:8.5px;color:#fff}
.search{left:628px;top:31px;width:136px;height:18px;border-radius:9px;background:#fff;overflow:hidden;display:flex}
.search span{flex:1;font-size:8px;color:#aaa;padding:4px 0 0 9px}
.search i{width:20px;background:var(--search-green);display:flex;align-items:center;justify-content:center}
.main-nav{top:61px;font-size:12px;font-weight:700;color:var(--nav-blue);text-transform:uppercase;letter-spacing:.1px}
.intro{left:120px;top:106px;width:600px;font-family:"Noto Serif",Georgia,serif;font-style:italic;font-size:15.5px;line-height:20px;color:#fff}
.intro b{font-weight:700}
.learn-more{left:660px;top:148px;font-family:"Noto Serif",Georgia,serif;font-style:italic;font-size:15px;color:#fff}
.learn-more span{color:var(--nav-blue)}

/* feature panel */
.feature-panel{left:108px;top:175px;width:652px;height:304px;border:1px solid #cfe6f7;border-radius:4px;
  background:radial-gradient(ellipse at 50% 40%,#2a93dc 0%,var(--panel-blue) 50%,var(--panel-blue-dark) 100%)}
.feature-card{top:190px;width:191px;height:210px;border:2px solid #fff;border-radius:5px;text-align:center;color:#fff}
.feature-card .kicker{margin-top:10px;font-size:12.5px}
.feature-card h2{font-weight:400;font-size:20px;line-height:22px;margin-top:2px}
.card-orange{left:123px;background:linear-gradient(180deg,var(--orange),var(--orange-dark))}
.card-green{left:338px;background:linear-gradient(180deg,var(--green),var(--green-dark))}
.card-rust{left:554px;background:linear-gradient(180deg,var(--rust),var(--rust-dark))}
.feature-art{top:272px;width:190px;height:190px;border-radius:50%;border:4px solid #e9e9e9;
  background:radial-gradient(circle at 50% 40%,#ffffff 0%,#f3f3f3 70%,#dcdcdc 100%);box-shadow:0 2px 6px rgba(0,0,0,.3)}
.find-btn{top:452px;width:96px;height:20px;border-radius:5px;color:#fff;font-size:13px;text-align:center;line-height:20px}

/* get started */
.start-box{left:95px;top:513px;width:677px;height:278px;background:var(--box-grey);border:1px solid var(--line-grey);border-radius:4px}
.meter-panel{left:96px;top:514px;width:227px;height:276px;background:linear-gradient(180deg,#fdfdfd,#ececec);border-right:1px solid var(--line-grey);border-radius:4px 0 0 4px;text-align:center}
.meter-panel h3{font-weight:400;font-size:16.5px;line-height:18px;margin-top:13px}
.meter-art{left:133px;top:578px;width:152px;height:152px;border-radius:50%;
  background:radial-gradient(circle,#3a3a3a 0%,#1d1d1d 62%,#c9c9c9 64%,#f2f2f2 80%,#bdbdbd 100%)}
.meter-cta{left:96px;top:750px;width:227px;text-align:center;font-weight:700;font-size:15px}
.start-title{left:338px;top:530px;font-size:21px;font-weight:400}
.list-card{top:573px;width:203px;height:204px;background:#fff;border:1px solid var(--line-grey);border-radius:5px;padding:10px 13px}
.list-card h4{font-family:Arial,sans-serif;font-size:11.5px;color:var(--link-blue);padding-bottom:8px;border-bottom:1px dotted #aaa;margin-bottom:8px}
.list-card ul{list-style:none}
.list-card li{font-family:Arial,sans-serif;font-size:8.5px;color:var(--text-mid);height:17px;display:flex;align-items:center;gap:6px}
.list-card li::before{content:"";width:8px;height:8px;border-radius:50%;background:#8ec6ea}
.list-card .more{font-family:Arial,sans-serif;font-size:8.5px;color:var(--link-blue);margin-top:5px}

/* inspiration */
.section-title{left:102px;top:806px;font-size:20px;color:var(--link-blue)}
.carousel{left:98px;top:842px;width:671px;height:153px;background:var(--carousel);border-left:5px solid var(--carousel-edge);border-right:5px solid var(--carousel-edge);border-radius:3px}
.arrow{top:914px;width:12px;height:18px;background:var(--carousel-edge);display:flex;align-items:center;justify-content:center}
.photo{top:856px;width:139px;height:93px;border:3px solid #fff}
.photo-a{background:linear-gradient(135deg,#8a5a42,#c7b4a0)}
.photo-b{background:linear-gradient(135deg,#b7b1a6,#6f6c6b)}
.photo-c{background:linear-gradient(135deg,#3d6fb0,#9fb7d6)}
.photo-d{background:linear-gradient(135deg,#d9dde4,#6a7c95)}
.caption{top:961px;font-family:Arial,sans-serif;font-size:9.5px;line-height:12px;color:#fff}

/* footer */
.site-footer{left:0;top:1023px;width:868px;height:177px;background:linear-gradient(180deg,var(--footer-top),var(--footer-bottom))}
.footer-mark{left:103px;top:1045px;width:92px;height:92px;border-radius:50%;background:rgba(255,255,255,.85)}
.footer-col{top:1041px;font-size:9px;color:var(--footer-link);line-height:15.8px}
.footer-col h5{font-size:11px;color:#fff;margin-bottom:5px}
.footer-col .more{color:var(--accent-yellow)}
.footer-rule{left:100px;top:1163px;width:668px;height:1px;background:rgba(255,255,255,.18)}
.copyright{left:103px;top:1173px;font-size:9px;color:#fff}
.share{left:664px;top:1174px;font-size:12px;color:#fff}
.share-box{top:1173px;width:16px;height:16px;border-radius:2px;background:#5e86c9}
.share-box.alt{background:#5cc3ee}
</style>
</head>
<body>
<div class="abs top-band"></div>

<header class="abs site-header"></header>
<div class="abs brand"><span class="brand-mark"></span><span class="brand-name">Lorvika</span></div>
<div class="abs brand-tagline">Entreprenørielle metoder i undervisningen</div>
<div class="abs search"><span>search...</span><i><svg width="9" height="9" viewBox="0 0 10 10"><circle cx="4" cy="4" r="3" fill="none" stroke="#fff" stroke-width="1.5"/><line x1="6.2" y1="6.2" x2="9" y2="9" stroke="#fff" stroke-width="1.6"/></svg></i></div>
<nav>
  <div class="abs main-nav" style="left:421px">Best practice schools</div>
  <div class="abs main-nav" style="left:571px">Lorvikameter</div>
  <div class="abs main-nav" style="left:671px">About lorvika.no</div>
</nav>
<p class="abs intro"><b>Pedagogical entrepreneurship works.</b> Lorem ipsum dolor sit amet, consectetur adipisicing elit, sed do eiusmod tempor incididunt ut labore et dolore magna aliqua.</p>
<div class="abs learn-more">Learn more <span>›</span></div>

<section>
  <div class="abs feature-panel"></div>
  <div class="abs feature-card card-orange"><p class="kicker">Learn about what, why and how!</p><h2>What is pedagogical entrepreneurship?</h2></div>
  <div class="abs feature-card card-green"><p class="kicker">Plan your lessons!</p><h2>Methods and teaching plans</h2></div>
  <div class="abs feature-card card-rust"><p class="kicker">Be inspired!</p><h2>Good examples / best practice</h2></div>
  <div class="abs feature-art" style="left:124px" role="img" aria-label="Hand-drawn sketch listing solution: what, why, how"></div>
  <div class="abs feature-art" style="left:339px" role="img" aria-label="Hand-drawn sketch of a lesson plan rising from idea to success"></div>
  <div class="abs feature-art" style="left:555px" role="img" aria-label="Hand-drawn sketch of a figure with a light bulb idea"></div>
  <div class="abs find-btn" style="left:171px;background:var(--orange-dark)">Find out more</div>
  <div class="abs find-btn" style="left:386px;background:var(--green)">Find out more</div>
  <div class="abs find-btn" style="left:602px;background:var(--rust-dark)">Find out more</div>
</section>

<section>
  <div class="abs start-box"></div>
  <div class="abs meter-panel"><h3>Are you working<br>entrepreneurship-like?</h3></div>
  <div class="abs meter-art" role="img" aria-label="Speedometer gauge illustration"></div>
  <div class="abs meter-cta">Try the lorvikameter!</div>
  <h2 class="abs start-title">Get started!</h2>
  <div class="abs list-card" style="left:338px">
    <h4>Methods</h4>
    <ul><li>Cafe-pedagogikk</li><li>Elevbedrift</li><li>Grundercamp</li><li>Story line</li><li>REAL</li><li>Grundercamp</li><li>Story line</li><li>REAL</li></ul>
    <p class="more">See more...</p>
  </div>
  <div class="abs list-card" style="left:555px">
    <h4>Teaching plans</h4>
    <ul><li>Teaching plans title</li><li>Teaching plans title</li><li>Teaching plans title</li><li>Teaching plans title</li><li>Teaching plans title</li><li>Teaching plans title</li><li>Teaching plans title</li><li>Teaching plans title</li></ul>
    <p class="more">See more...</p>
  </div>
</section>

<section>
  <h2 class="abs section-title" style="font-weight:400">Inspiration</h2>
  <div class="abs carousel"></div>
  <div class="abs arrow" style="left:103px"><svg width="6" height="8" viewBox="0 0 6 8"><path d="M5 0 1 4 5 8" fill="none" stroke="#fff" stroke-width="1.4"/></svg></div>
  <div class="abs arrow" style="left:753px"><svg width="6" height="8" viewBox="0 0 6 8"><path d="M1 0 5 4 1 8" fill="none" stroke="#fff" stroke-width="1.4"/></svg></div>
  <div class="abs photo photo-a" style="left:123px" role="img" aria-label="Photo of students working together around a table"></div>
  <div class="abs photo photo-b" style="left:284px" role="img" aria-label="Photo of adults taking notes at a seminar"></div>
  <div class="abs photo photo-c" style="left:445px" role="img" aria-label="Photo of a teacher in a classroom"></div>
  <div class="abs photo photo-d" style="left:606px" role="img" aria-label="Photo of a cheering group"></div>
  <p class="abs caption" style="left:123px">Lorem ipsum dolor<br>sed do eiusmod</p>
  <p class="abs caption" style="left:284px">Lorem ipsum dolor<br>sed do eiusmod</p>
  <p class="abs caption" style="left:445px">Lorem ipsum dolor<br>sed do eiusmod</p>
  <p class="abs caption" style="left:606px">Lorem ipsum dolor<br>sed do eiusmod</p>
</section>

<footer>
  <div class="abs site-footer"></div>
  <div class="abs footer-mark"></div>
  <div class="abs footer-col" style="left:227px"><h5>Pedagogical entrepreneurship</h5>What is pedagogical entrepreneurship?<br>Science<br>Best practice schools<br>Lorvikameter<br>About lorvika.no</div>
  <div class="abs footer-col" style="left:425px"><h5>Methoda</h5>Storyline<br>REAL<br>Cafe-pedagogikk<br><span class="more">See more...</span></div>
  <div class="abs footer-col" style="left:540px"><h5>Teaching plans</h5>Lorem ipsum dolor<br>sed do eiusmod<br>Lorem ipsum dolor<br>sed do eiusmod<br><span class="more">See more...</span></div>
  <div class="abs footer-col" style="left:666px"><h5>Gode eksemplert</h5>Lorem ipsum dolor<br>sed do eiusmod<br>Lorem ipsum dolor<br>sed do eiusmod<br><span class="more">See more...</span></div>
  <div class="abs footer-rule"></div>
  <div class="abs copyright">© 2011 Pedagogical entrepreneurship.</div>
  <div class="abs share">Share this!</div>
  <div class="abs share-box" style="left:720px"></div>
  <div class="abs share-box alt" style="left:741px"></div>
</footer>
</body>
</html>
```